Popup Nightclub Grand Opening Flyer

We need to design a flyer for the grand opening of an upscale, exclusive nightclub called "Lanternfall". The design needs to be chic and exclusive. The background should be black and the text should primarily be white. We like minimalist designs.

Here is the text for the flyer
-
Velvetrope Atlanta Presents

Lanternfall (LOGO)

A Popup Nightclub Experience
For one night Only

Friday, October 18, 2013
Party begins at 9PM

INVITE ONLY

See invitation for location details
(Velvetrope Atlanta logo)

-
Examples we like

http://cdn2-b.brivelpost.com/sites/default/files/styles/image_content_width/hash/3d/fa/1472093815_4471_flyer.jpg?itok=R8kqWm2z

http://api.plovra.com/files/7Kqq-Tr82XXB3pQzJvmtR5HL2W719E4nbRtC6KLd4HsfM8Y2qTDK-VmjwDoNqLX4QBzTHD9nakRbVx3m-Pfq8htc3MDTWr5p4/2zelSaturdays.jpg

http://quenmar.com/wp-content/uploads/yootheme/widgetkit/gallery/2zel/2zel-gen_vroom4-01.jpg

Hi All, one thing that we are seeing that we don't like is on over emphasis on the phrase "a popup nightclub experience" please don't make this the largest thing on the flyer

Target Market(s)

Target market is 25-35 year olds who are affluent (rich) and like luxury brands

Requirements
Must have
• Dark Background
Nice to have
• Velvetrope Logo on the bottom
Modern text that isn't curvy
Should not have
• Curved text

```html
<!DOCTYPE html>
<html lang="en">
<head>
<meta charset="utf-8">
<title>Lanternfall – Popup Nightclub Flyer</title>
<link rel="stylesheet" href="https://fonts.googleapis.com/css2?family=Jost:wght@300;400&family=Oswald:wght@300;400;500&family=Barlow:wght@300;400&display=swap">
<style>
  :root {
    --ink: #000000;
    --ember: #2a1d18;
    --ember-soft: #1a1210;
    --white: #ffffff;
    --silver-hi: #e6e6e6;
    --silver-lo: #8a8a8a;
    --grey: #b4b4b4;
    --rule: #8f8f8f;
  }
  * { margin: 0; padding: 0; box-sizing: border-box; }
  html, body {
    width: 871px; height: 1200px; overflow: hidden;
    background: var(--ink);
  }
  .flyer {
    position: relative;
    width: 871px; height: 1200px;
    background: var(--ink);
    color: var(--white);
    text-align: center;
    overflow: hidden;
  }
  .flyer__ornament {
    position: absolute; inset: 0;
    background:
      radial-gradient(ellipse 260px 120px at 50% 310px, var(--ember) 0%, transparent 70%),
      radial-gradient(ellipse 200px 90px at 22% 215px, var(--ember-soft) 0%, transparent 75%),
      radial-gradient(ellipse 200px 90px at 78% 215px, var(--ember-soft) 0%, transparent 75%),
      radial-gradient(ellipse 180px 70px at 22% 890px, var(--ember-soft) 0%, transparent 75%),
      radial-gradient(ellipse 180px 70px at 78% 890px, var(--ember-soft) 0%, transparent 75%),
      radial-gradient(ellipse 170px 190px at 50% 650px, #1c1c1c 0%, transparent 75%);
  }
  .line {
    position: absolute; left: 0; right: 0;
    white-space: nowrap;
  }
  .presenter {
    top: 116px;
    font-family: "Jost", sans-serif; font-weight: 400;
    font-size: 32px; line-height: 36px;
  }
  .presents {
    top: 160px;
    font-family: "Jost", sans-serif; font-weight: 300;
    font-size: 23px; line-height: 28px; letter-spacing: 9px;
    padding-left: 9px;
  }
  .brand-mark {
    position: absolute; left: 50%; top: 250px;
    width: 90px; height: 90px; margin-left: -45px;
    border-radius: 50%;
    background: linear-gradient(180deg, var(--silver-hi), var(--silver-lo));
  }
  .brand-name {
    top: 372px;
    font-family: "Jost", sans-serif; font-weight: 300;
    font-size: 52px; line-height: 56px; letter-spacing: 8px;
    padding-left: 8px;
  }
  .brand-sub {
    top: 434px;
    font-family: "Jost", sans-serif; font-weight: 300;
    font-size: 21px; line-height: 24px; letter-spacing: 4px;
    padding-left: 4px;
  }
  .rule {
    position: absolute; left: 50%;
    height: 2px; margin-left: -132px; width: 264px;
    background: linear-gradient(90deg, transparent, var(--rule) 15%, var(--silver-hi) 50%, var(--rule) 85%, transparent);
  }
  .rule--top { top: 540px; }
  .rule--mid { top: 712px; }
  .rule--low { top: 765px; }
  .tagline {
    position: absolute; left: 0; right: 0; top: 550px;
    font-family: "Oswald", sans-serif; font-weight: 500;
    font-size: 44px; line-height: 52px;
    text-transform: uppercase;
    background: linear-gradient(180deg, var(--silver-hi) 0%, var(--silver-lo) 60%, #c8c8c8 100%);
    -webkit-background-clip: text; background-clip: text;
    color: transparent;
  }
  .once {
    top: 723px;
    font-family: "Barlow", sans-serif; font-weight: 400;
    font-size: 24px; line-height: 30px; letter-spacing: 0.5px;
  }
  .dotted {
    position: absolute; left: 50%;
    width: 318px; margin-left: -159px;
    border-top: 2px dotted var(--grey);
  }
  .dotted--top { top: 846px; }
  .dotted--bottom { top: 926px; }
  .date {
    top: 855px;
    font-family: "Oswald", sans-serif; font-weight: 500;
    font-size: 28px; line-height: 32px;
    text-transform: uppercase;
  }
  .time {
    top: 888px;
    font-family: "Oswald", sans-serif; font-weight: 300;
    font-size: 27px; line-height: 31px; letter-spacing: 0.5px;
    text-transform: uppercase;
  }
  .invite {
    top: 954px;
    font-family: "Oswald", sans-serif; font-weight: 400;
    font-size: 20px; line-height: 24px; letter-spacing: 6px;
    padding-left: 6px;
    text-transform: uppercase;
  }
  .location-note {
    top: 1010px;
    font-family: "Barlow", sans-serif; font-weight: 300;
    font-size: 17px; line-height: 20px; letter-spacing: 1px;
    color: var(--grey);
  }
  .host {
    position: absolute; left: 0; right: 0; top: 1052px;
    display: flex; justify-content: center; align-items: center; gap: 14px;
  }
  .host__mark {
    width: 26px; height: 26px; border: 2px solid var(--white);
  }
  .host__name {
    font-family: "Jost", sans-serif; font-weight: 400;
    font-size: 24px; line-height: 28px; letter-spacing: 3px;
    text-transform: uppercase;
  }
</style>
</head>
<body>
  <main class="flyer">
    <div class="flyer__ornament" role="img" aria-label="Dark ember-toned symmetrical petal ornament glowing softly behind the text"></div>

    <p class="line presenter">Velvetrope Atlanta</p>
    <p class="line presents">Presents</p>

    <div class="brand-mark"></div>
    <h1 class="line brand-name">LANTERNFALL</h1>
    <p class="line brand-sub">NIGHTCLUB</p>

    <div class="rule rule--top"></div>
    <h2 class="tagline">A Popup<br>Nightclub<br>Experience</h2>
    <div class="rule rule--mid"></div>
    <p class="line once">For one night only</p>
    <div class="rule rule--low"></div>

    <div class="dotted dotted--top"></div>
    <p class="line date">Friday, October 18, 2013</p>
    <p class="line time">Party begins at 9PM</p>
    <div class="dotted dotted--bottom"></div>

    <p class="line invite">Invite Only</p>

    <p class="line location-note">See invitation for location details</p>

    <div class="host">
      <span class="host__mark"></span>
      <span class="host__name">Velvetrope Atlanta</span>
    </div>
  </main>
</body>
</html>
```